Party planning business card design

Revels with Kit is a party planning business

Function Planning: Weddings/Themed Parties/Children's Parties

Adult and Children's Photo Booths
Party Themed boxes,
We can find the venue, entertainment. face painters.

Children's costumes and accessories - Sell / Hire

Web: www.revelswithkit.example
Facebook: Revels with Kit

Industry/Entity Type

Party Planning

Contact Information for Business Card

Revels With Kit, Rosalind Trevick,
Creative Director

Colors
e34297
000000

Requirements
Must have
• on my logo are you able to edit the stars to pink?

```html
<!DOCTYPE html>
<html lang="en">
<head>
<meta charset="utf-8">
<title>Revels with Kit – Business Card</title>
<link href="https://fonts.googleapis.com/css2?family=Lato:wght@400;700;900&display=swap" rel="stylesheet">
<style>
  :root {
    --pink: #e34297;
    --pink-deep: #c42d7f;
    --ink: #111111;
    --paper: #f7f7f7;
    --stage: #2b2b2b;
    --photo-dark: #2a0d12;
    --photo-red: #8a2a2a;
  }
  * { box-sizing: border-box; margin: 0; padding: 0; }
  html, body { width: 1200px; height: 900px; overflow: hidden; }
  body {
    background: var(--stage);
    font-family: "Lato", Arial, sans-serif;
    position: relative;
  }
  .card {
    position: absolute;
    width: 560px;
    height: 320px;
    border-radius: 18px;
    overflow: hidden;
    box-shadow: 0 14px 30px rgba(0,0,0,.5);
  }

  /* Front */
  .card--front { left: 60px; top: 60px; background: var(--pink); }
  .front__photo {
    position: absolute; inset: 0;
    background:
      radial-gradient(circle at 62% 18%, rgba(255,200,160,.85) 0 3%, transparent 10%),
      linear-gradient(180deg, var(--photo-dark) 0%, var(--photo-red) 38%, var(--pink) 72%, var(--pink) 100%);
  }
  .front__title {
    position: absolute; left: 0; right: 0; top: 196px;
    text-align: center; color: #fff;
    font-weight: 700; font-size: 30px; letter-spacing: 1.5px;
  }
  .front__rule {
    position: absolute; left: 150px; right: 150px; top: 240px;
    height: 2px; background: rgba(40,10,20,.7);
  }
  .front__tagline {
    position: absolute; left: 0; right: 0; top: 250px;
    text-align: center; color: var(--ink);
    font-weight: 900; font-size: 24px; letter-spacing: 1px;
  }

  /* Back */
  .card--back { left: 580px; top: 520px; background: var(--paper); }
  .back__shapes { position: absolute; inset: 0; }
  .brand {
    position: absolute; left: 34px; top: 92px;
    display: flex; align-items: center; gap: 10px;
  }
  .brand__dot { width: 22px; height: 22px; border-radius: 50%; background: var(--pink); }
  .brand__name { font-size: 24px; font-weight: 700; color: var(--ink); letter-spacing: 1px; }

  .contact {
    position: absolute; right: 18px; top: 22px;
    text-align: right; color: var(--ink);
  }
  .contact__name { color: var(--pink); font-weight: 900; font-size: 20px; letter-spacing: .5px; }
  .contact__role { font-weight: 700; font-size: 13px; margin-bottom: 10px; }
  .contact__line {
    display: flex; justify-content: flex-end; align-items: center; gap: 7px;
    font-weight: 700; font-size: 13px; line-height: 20px;
  }
  .contact__line svg { width: 14px; height: 14px; fill: var(--pink); flex: none; }
  .contact__line--spaced { margin-top: 10px; }
  .contact__web span { color: var(--pink); }
  .contact__line--web { padding-right: 21px; }

  .band-text {
    position: absolute; top: 184px;
    color: #fff; font-weight: 700; font-size: 12.5px; line-height: 16px;
    text-align: center; letter-spacing: .3px;
  }
  .band-text--left { left: 40px; width: 240px; }
  .band-text--right { left: 300px; width: 240px; }

  .services {
    position: absolute; left: 0; right: 0; top: 240px;
    text-align: center; font-weight: 900; font-size: 15px; color: var(--ink);
  }
  .services .sep { display: inline-block; width: 3px; height: 16px; background: var(--pink); vertical-align: -2px; margin: 0 6px; }
</style>
</head>
<body>

<section class="card card--front">
  <div class="front__photo" role="img" aria-label="Photograph of friends laughing and dancing at a party under warm stage lights"></div>
  <h1 class="front__title">Revels with Kit</h1>
  <div class="front__rule"></div>
  <p class="front__tagline">We get the Party Started</p>
</section>

<section class="card card--back">
  <svg class="back__shapes" viewBox="0 0 560 320" preserveAspectRatio="none" aria-hidden="true">
    <path d="M0 0 H560 V0 Q545 14 520 14 L440 14 Q420 14 405 20 L0 20 Z" fill="var(--pink)"/>
    <path d="M0 0 H560 V16 H0 Z" fill="var(--pink)"/>
    <rect x="0" y="176" width="560" height="48" fill="var(--pink)"/>
    <path d="M0 284 H150 Q170 284 185 276 Q200 268 220 268 H560 V320 H0 Z" fill="var(--pink)"/>
    <path d="M0 290 H150 Q175 290 190 300 Q205 310 230 310 H0 Z" fill="var(--pink-deep)" opacity=".35"/>
  </svg>

  <div class="brand">
    <span class="brand__dot"></span>
    <span class="brand__name">Revels with Kit</span>
  </div>

  <div class="contact">
    <div class="contact__name">ROSALIND</div>
    <div class="contact__role">Managing Director</div>
    <div class="contact__line">Harbourvale, Queensland, Australia 4999
      <svg viewBox="0 0 16 16"><path d="M8 1 L15 8 H13 V15 H9.5 V10.5 H6.5 V15 H3 V8 H1 Z"/></svg></div>
    <div class="contact__line">0400123987
      <svg viewBox="0 0 16 16"><path d="M2 6 Q8 1 14 6 L12.5 8 L10.5 7 V5.5 Q8 4.8 5.5 5.5 V7 L3.5 8 Z M4 9 H12 L13 14 H3 Z"/></svg></div>
    <div class="contact__line contact__line--spaced">rosalind@revelswithkit.example
      <svg viewBox="0 0 16 16"><path d="M1 3 H15 V13 H1 Z M2 4 L8 9 L14 4" stroke="#fff" stroke-width="1"/></svg></div>
    <div class="contact__line contact__web">www.<span>revelswithkit</span>.example
      <svg viewBox="0 0 16 16"><circle cx="8" cy="8" r="7"/><path d="M1 8 H15 M8 1 Q4 8 8 15 M8 1 Q12 8 8 15" stroke="#fff" stroke-width="1" fill="none"/></svg></div>
  </div>

  <p class="band-text band-text--left">ADULT &amp; CHILDREN'S PHOTO<br>BOOTHS &amp; PARTY THEMED BOXES</p>
  <p class="band-text band-text--right">WE CAN FIND THE VENUE,<br>ENTERTAINMENT. FACE PAINTERS.</p>

  <p class="services">WEDDINGS<span class="sep"></span>THEMED PARTIES<span class="sep"></span>CHILDREN'S PARTIES</p>
</section>

</body>
</html>
```